Introductory Postcard

We need 2 introductory postcard designed. We're a new foundation. We're mailing these postcards to potential sponsors and business partners. You can go to our website "pebbleharborfund.org" for a briefing of our foundation. When using my logo please delete Inc. We want to introduce our foundation and give them a few reasons why they should be a part of it.

Target Market(s)

Potential sponsors and business partners. We are looking for monetary and brand new shoe support. We're looking to build up shoe inventory so we need shoes. We're willing to purchase shoes as well.

Industry/Entity Type

Business

Requirements
Must have
• The same color scheme as the website. 1st postcard should target shoe stores. We need brand new shoe inventory, so shoe stores are a target. 2nd postcard should target professional sponsors such as lawyers, doctors, dentist, etc.
Should not have
• Nothing over the top. Postcard should be clean, simple, and informative.

```html
<!DOCTYPE html>
<html lang="en">
<head>
<meta charset="utf-8">
<title>Pebble Harbor Fund – Introductory Postcards</title>
<link rel="stylesheet" href="https://fonts.googleapis.com/css2?family=Tinos:wght@400;700&display=swap">
<style>
  :root {
    --page-bg: #000000;
    --card-bg: #ffffff;
    --brand-red: #ee1c1c;
    --ink: #111111;
    --panel-grey: #ebebeb;
    --rule: #1a1a1a;
    --white: #ffffff;
    --photo-child: #9a9a9a;
    --photo-man: #3c3c3c;
    --sneaker-pink: #f3c6e4;
  }
  * { box-sizing: border-box; margin: 0; padding: 0; }
  html, body {
    width: 809px; height: 1200px; overflow: hidden;
    background: var(--page-bg);
    font-family: "Tinos", "Times New Roman", serif;
    color: var(--ink);
  }
  .canvas { position: relative; width: 809px; height: 1200px; }

  .postcard {
    position: absolute; left: 65px; width: 686px; height: 530px;
    background: var(--card-bg); overflow: hidden;
  }
  .postcard--stores { top: 47px; }
  .postcard--sponsors { top: 615px; }
  .postcard > * { position: absolute; }

  .brand { left: 20px; top: 22px; display: flex; align-items: center; gap: 8px; }
  .brand__dot { width: 26px; height: 26px; border-radius: 50%; background: var(--brand-red); }
  .brand__name { font-size: 24px; font-weight: 400; color: var(--ink); }

  .stamp-box {
    left: 582px; top: 19px; width: 77px; height: 88px;
    border: 3px solid #444; border-bottom: none;
  }

  .tagline-band {
    left: 7px; top: 82px; width: 671px; height: 25px;
    background: var(--brand-red); color: var(--white);
    font-size: 14px; line-height: 25px; padding-left: 8px; letter-spacing: .2px;
  }

  .info-panel { left: 7px; top: 107px; width: 335px; height: 375px; background: var(--panel-grey); }
  .intro {
    left: 14px; top: 116px; width: 300px;
    font-size: 18px; line-height: 20px;
  }
  .photo { top: 229px; height: 173px; }
  .photo--child { left: 7px; width: 131px; background: linear-gradient(160deg, #c4c4c4, var(--photo-child)); }
  .photo--elder { left: 145px; width: 180px; background: linear-gradient(160deg, #6a6a6a, var(--photo-man) 60%, #1d1d1d); }
  .photo--sneaker {
    left: 49px; top: 226px; width: 218px; height: 190px;
    background:
      radial-gradient(ellipse 38% 48% at 52% 52%, #2e2e2e 0%, #6d6d6d 70%, rgba(109,109,109,0) 100%),
      radial-gradient(ellipse 50% 50% at 45% 40%, var(--sneaker-pink) 0%, rgba(243,198,228,0) 100%);
  }

  .address {
    left: 40px; top: 412px;
    font-size: 15px; font-weight: 700; line-height: 22px; font-style: normal;
  }
  .corner-mark {
    left: 7px; top: 450px; width: 0; height: 0;
    border-left: 34px solid var(--brand-red); border-top: 32px solid transparent;
  }

  .appeal-box {
    left: 342px; top: 107px; width: 336px; height: 195px;
    background: #000; color: var(--white); padding: 10px 30px 0 20px;
  }
  .appeal-box__text { font-size: 22px; line-height: 24px; }
  .appeal-box__contact {
    position: absolute; left: 20px; bottom: 16px; right: 16px;
    display: flex; align-items: center; justify-content: space-between;
  }
  .phone { display: flex; align-items: center; gap: 8px; font-size: 22px; font-weight: 700; }
  .social { font-size: 15px; font-weight: 700; }

  .address-line { left: 360px; width: 302px; height: 2px; background: var(--rule); }
  .address-line--1 { top: 358px; }
  .address-line--2 { top: 391px; }
  .address-line--3 { top: 425px; }
  .address-line--4 { top: 458px; }

  .footer-band {
    left: 7px; top: 482px; width: 671px; height: 39px;
    background: var(--brand-red); color: var(--white);
    display: flex; align-items: center; justify-content: space-between;
    padding: 0 14px 0 38px;
  }
  .footer-band__url { font-size: 19px; }
  .payments { display: flex; gap: 12px; font-size: 15px; font-weight: 700; }
</style>
</head>
<body>
<main class="canvas">

  <section class="postcard postcard--stores" aria-label="Postcard for shoe stores">
    <div class="brand"><span class="brand__dot"></span><span class="brand__name">Pebble Harbor Fund</span></div>
    <div class="stamp-box"></div>
    <div class="tagline-band">REBUILDING LIVES ONE STEP AT A TIME...</div>
    <div class="info-panel"></div>
    <p class="intro">Pebble Harbor Fund is a nonprofit irs recognized 501(c)(3) business devoted to providing new shoes to men,women,and children in need of them.</p>
    <div class="photo photo--child" role="img" aria-label="Black and white portrait of a smiling little girl"></div>
    <div class="photo photo--elder" role="img" aria-label="Black and white portrait of an elderly bearded man"></div>
    <address class="address">1480 LANTERN WAY #8<br>BAYHOLLOW,FL.33990<br>786-555-0182</address>
    <div class="corner-mark"></div>
    <div class="appeal-box">
      <p class="appeal-box__text">Shoe stores: donate brand new pairs or sell us stock at partner prices to build our shoe inventory.</p>
      <div class="appeal-box__contact">
        <span class="phone">
          <svg width="26" height="26" viewBox="0 0 26 26" aria-hidden="true"><circle cx="13" cy="13" r="11.5" fill="none" stroke="#fff" stroke-width="2"/><path d="M9 7.5l2.2-.5 1.3 3-1.5 1.2c.7 1.5 1.8 2.6 3.3 3.3l1.2-1.5 3 1.3-.5 2.2c-4.6.4-9.4-4.4-9-9z" fill="#fff"/></svg>
          410-555-0147
        </span>
        <span class="social">Chatterlink</span>
      </div>
    </div>
    <div class="address-line address-line--1"></div>
    <div class="address-line address-line--2"></div>
    <div class="address-line address-line--3"></div>
    <div class="address-line address-line--4"></div>
    <div class="footer-band">
      <span class="footer-band__url">www.pebbleharborfund.org</span>
      <span class="payments"><span>Paylane</span><span>Cardwise</span></span>
    </div>
  </section>

  <section class="postcard postcard--sponsors" aria-label="Postcard for professional sponsors">
    <div class="brand"><span class="brand__dot"></span><span class="brand__name">Pebble Harbor Fund</span></div>
    <div class="stamp-box"></div>
    <div class="tagline-band">REBUILDING LIVES ONE STEP AT A TIME...</div>
    <div class="info-panel"></div>
    <p class="intro">Pebble Harbor Fund is a nonprofit irs recognized 501(c)(3) business devoted to providing new shoes to men,women,and children in need of them.</p>
    <div class="photo--sneaker" role="img" aria-label="Illustration of a black canvas sneaker with pink swirl decoration"></div>
    <address class="address">1480 LANTERN WAY #8<br>BAYHOLLOW,FL.33990<br>786-555-0182</address>
    <div class="corner-mark"></div>
    <div class="appeal-box">
      <p class="appeal-box__text">Lawyers, doctors and dentists: sponsor us with monetary contributions that will go toward new shoes.</p>
      <div class="appeal-box__contact">
        <span class="phone">
          <svg width="26" height="26" viewBox="0 0 26 26" aria-hidden="true"><circle cx="13" cy="13" r="11.5" fill="none" stroke="#fff" stroke-width="2"/><path d="M9 7.5l2.2-.5 1.3 3-1.5 1.2c.7 1.5 1.8 2.6 3.3 3.3l1.2-1.5 3 1.3-.5 2.2c-4.6.4-9.4-4.4-9-9z" fill="#fff"/></svg>
          410-555-0147
        </span>
        <span class="social">Chatterlink</span>
      </div>
    </div>
    <div class="address-line address-line--1"></div>
    <div class="address-line address-line--2"></div>
    <div class="address-line address-line--3"></div>
    <div class="address-line address-line--4"></div>
    <div class="footer-band">
      <span class="footer-band__url">www.pebbleharborfund.org</span>
      <span class="payments"><span>Paylane</span><span>Cardwise</span></span>
    </div>
  </section>

</main>
</body>
</html>
```